Boarding Pass for Tour Company

We need an A6 sized boarding pass desinged for our tour company.

Colours to follow company logo. Image background with white text on top.

Require a strip at the bottom with text on top. This will be a group indicator colour. Can use purple for design.

Font styles to use
Sans Serif

Colors
0054AA
0677BA
7BADD7
CADEEF
E8F1F8

```html
<!DOCTYPE html>
<html lang="en">
<head>
<meta charset="utf-8">
<title>Skyward Drifts Boarding Pass</title>
<link rel="stylesheet" href="https://fonts.googleapis.com/css2?family=Montserrat:wght@400;800&family=Dancing+Script:wght@700&family=EB+Garamond:ital@1&family=Oswald:wght@600&display=swap">
<style>
  :root {
    --brand-deep: #0054AA;
    --brand-mid: #0677BA;
    --brand-light: #7BADD7;
    --brand-pale: #CADEEF;
    --brand-mist: #E8F1F8;
    --band: #00AEEF;
    --sky: #4FB8EA;
    --ink: #111111;
    --rule: #555555;
    --paper: #ffffff;
  }
  * { margin: 0; padding: 0; box-sizing: border-box; }
  html, body { width: 685px; height: 1200px; overflow: hidden; background: var(--paper); }
  .pass {
    position: relative; width: 685px; height: 1200px; overflow: hidden;
    background: var(--paper); font-family: "Montserrat", sans-serif;
  }
  .sky {
    position: absolute; left: 0; top: 0; width: 685px; height: 810px;
    background:
      radial-gradient(ellipse 260px 120px at 120px 60px, rgba(255,255,255,.95), transparent 70%),
      radial-gradient(ellipse 300px 90px at 520px 120px, rgba(255,255,255,.9), transparent 70%),
      radial-gradient(ellipse 200px 140px at 60px 520px, rgba(255,255,255,.85), transparent 70%),
      radial-gradient(ellipse 220px 160px at 640px 470px, rgba(255,255,255,.85), transparent 70%),
      radial-gradient(ellipse 420px 140px at 340px 760px, rgba(255,255,255,1), transparent 75%),
      linear-gradient(180deg, var(--sky) 0%, #6CC6EF 55%, var(--brand-mist) 88%, var(--paper) 100%);
  }
  .brand {
    position: absolute; top: 46px; left: 0; width: 100%;
    text-align: center; color: var(--brand-mid);
    font-weight: 800; font-size: 34px; letter-spacing: 1px;
  }
  .plane { position: absolute; }
  .plane-left { left: 92px; top: 148px; }
  .plane-right { left: 580px; top: 190px; }
  .flight-path { position: absolute; left: 0; top: 0; }
  .photo-card {
    position: absolute; top: 212px; width: 218px; height: 444px;
    background: var(--paper); border-radius: 14px; padding: 8px;
  }
  .photo-card.left { left: 108px; }
  .photo-card.right { left: 363px; }
  .photo {
    width: 100%; height: 100%; border-radius: 10px;
  }
  .photo.vineyard { background: linear-gradient(180deg, #E8D9A0 0%, #2A3244 30%, #3D5366 60%, #3E7A2E 80%, #2E5E22 100%); }
  .photo.open-sky { background: linear-gradient(180deg, #3E6FB8 0%, #3A2E22 25%, #4B3A25 50%, #8FB3D9 72%, #6F7A3A 100%); }
  .title {
    position: absolute; left: 0; top: 548px; width: 100%; text-align: center;
    font-family: "Dancing Script", cursive; font-weight: 700; font-size: 118px;
    color: var(--paper); line-height: 1;
    text-shadow: 3px 3px 0 var(--brand-mid);
  }
  .subtitle {
    position: absolute; left: 0; top: 680px; width: 100%; text-align: center;
    font-family: "EB Garamond", serif; font-style: italic; font-size: 40px; color: var(--ink);
  }
  .hashtag-band {
    position: absolute; left: 0; top: 838px; width: 100%; height: 50px;
    background: var(--band); color: var(--paper);
    font-size: 25px; font-weight: 400; text-align: center; line-height: 50px;
  }
  .tear-line {
    position: absolute; left: 0; top: 908px; width: 100%;
    border-top: 3px dashed #444;
  }
  .pilot {
    position: absolute; left: 0; top: 930px; width: 100%; text-align: center;
    font-family: "Oswald", sans-serif; font-weight: 600; font-size: 58px;
    color: var(--ink); letter-spacing: 1px;
  }
  .write-line {
    position: absolute; left: 40px; width: 605px; border-top: 2px solid var(--rule);
  }
  .write-line.one { top: 1032px; }
  .write-line.two { top: 1094px; }
  .write-line.three { top: 1150px; }
</style>
</head>
<body>
<main class="pass">
  <div class="sky" role="img" aria-label="Bright blue sky with soft white clouds"></div>

  <svg class="flight-path" width="685" height="810" viewBox="0 0 685 810" aria-hidden="true">
    <path d="M90 680 C 160 560, 380 520, 480 560 S 640 420, 630 230" fill="none" stroke="#ffffff" stroke-width="2" stroke-dasharray="6 5"/>
  </svg>

  <div class="brand">Skyward Drifts</div>

  <svg class="plane plane-left" width="56" height="44" viewBox="0 0 56 44" aria-hidden="true">
    <path d="M2 4 L54 22 L20 26 Z" fill="var(--brand-mid)"/>
    <path d="M20 26 L54 22 L28 42 Z" fill="var(--brand-light)"/>
  </svg>
  <svg class="plane plane-right" width="56" height="44" viewBox="0 0 56 44" aria-hidden="true">
    <path d="M54 4 L2 22 L36 26 Z" fill="#ffffff"/>
    <path d="M36 26 L2 22 L28 42 Z" fill="var(--brand-pale)"/>
  </svg>

  <div class="photo-card left">
    <div class="photo vineyard" role="img" aria-label="Hot air balloon with checked pattern rising over green vineyard rows"></div>
  </div>
  <div class="photo-card right">
    <div class="photo open-sky" role="img" aria-label="Hot air balloon with basket floating in a blue sky above trees"></div>
  </div>

  <div class="title">Boarding</div>
  <div class="subtitle">pass</div>

  <div class="hashtag-band">#skywarddrifts</div>
  <div class="tear-line"></div>

  <div class="pilot">PILOT:&nbsp; MARCO</div>
  <div class="write-line one"></div>
  <div class="write-line two"></div>
  <div class="write-line three"></div>
</main>
</body>
</html>
```